Stationery Design Project

I need a design that is simple, clean and modern, in square style, bold font.
The majority of the design needs to be White and Black with a splash of Red colour.
I would like a design for business cards and letter heads with the following information.
Name, Title, Phone, Fax, Email, Website and company ABN number

Target Market(s)

25 to 65 years old real estate clients

Industry/Entity Type

Business

Requirements
Must have
• All designs must incorporate Company Logo, Name, Title, Phone, Fax, Email, Website and company ABN number

```html
<!DOCTYPE html>
<html lang="en">
<head>
<meta charset="utf-8">
<title>Grey Heron Realty – Stationery</title>
<link href="https://fonts.googleapis.com/css2?family=Montserrat:wght@500;700&family=Open+Sans:wght@400;600&family=Dancing+Script:wght@500&display=swap" rel="stylesheet">
<style>
  :root {
    --backdrop: #e3e1e1;
    --paper: #ffffff;
    --ink: #1a1a1a;
    --ink-soft: #555555;
    --ink-muted: #8a8a8a;
    --accent: #d42a2a;
    --rule: #d9d9d9;
  }
  * { box-sizing: border-box; margin: 0; padding: 0; }
  html, body { width: 1200px; height: 843px; overflow: hidden; }
  body {
    background: var(--backdrop);
    font-family: "Open Sans", Arial, sans-serif;
    color: var(--ink);
    position: relative;
  }

  /* Brand name lockup */
  .brand {
    display: inline-flex;
    align-items: center;
    gap: 8px;
    font-family: "Montserrat", Arial, sans-serif;
    font-weight: 700;
    color: var(--ink);
    text-transform: uppercase;
    letter-spacing: 0.08em;
    white-space: nowrap;
  }
  .brand-square { display: inline-block; background: var(--accent); }

  /* Letterhead */
  .letterhead {
    position: absolute;
    left: 610px; top: 40px;
    width: 530px; height: 750px;
    background: var(--paper);
    box-shadow: 0 2px 6px rgba(0,0,0,0.15);
    padding: 60px 64px 0;
  }
  .letterhead .brand-row { text-align: center; margin-bottom: 60px; }
  .letterhead .brand { font-size: 17px; }
  .letterhead .brand-square { width: 12px; height: 12px; }
  .letter-body { font-size: 10.5px; line-height: 1.6; color: var(--ink-soft); }
  .letter-body .salutation { color: var(--ink); margin-bottom: 14px; }
  .letter-body p { margin-bottom: 12px; }
  .sign-off { margin-top: 26px; font-size: 10.5px; color: var(--ink-muted); }
  .signature {
    font-family: "Dancing Script", cursive;
    font-size: 22px; color: var(--ink-muted); margin: 4px 0 2px;
  }
  .letter-footer {
    position: absolute; left: 64px; right: 0; bottom: 0;
  }
  .letter-footer .company-line {
    font-family: "Montserrat", Arial, sans-serif; font-weight: 700;
    font-size: 9px; letter-spacing: 0.08em; text-transform: uppercase;
    color: var(--ink); margin-bottom: 6px; padding-right: 64px; text-align: right;
  }
  .letter-footer .footer-rule { height: 1px; background: var(--accent); margin-right: 64px; }
  .letter-footer .contact-row {
    display: flex; justify-content: space-between;
    font-size: 8.5px; color: var(--ink-soft);
    padding: 8px 64px 18px 0;
  }
  .letter-footer .contact-row b { color: var(--accent); font-weight: 600; }
  .edge-bands { display: flex; height: 7px; margin-left: -64px; }
  .edge-bands .band-dark { flex: 1; background: var(--ink); }
  .edge-bands .band-accent { width: 130px; background: var(--accent); }

  /* Business cards */
  .card {
    position: absolute; left: 80px;
    width: 400px; height: 228px;
    background: var(--paper);
    box-shadow: 0 2px 6px rgba(0,0,0,0.15);
  }
  .card-front { top: 150px; display: flex; flex-direction: column; align-items: center; justify-content: center; }
  .card-front .brand { font-size: 18px; }
  .card-front .brand-square { width: 13px; height: 13px; }
  .card-front .card-web {
    position: absolute; bottom: 22px; font-size: 9px; color: var(--ink-soft);
  }
  .card-back { top: 410px; display: flex; align-items: center; padding: 0 26px; }
  .card-back .brand { font-size: 12.5px; gap: 6px; }
  .card-back .brand-square { width: 9px; height: 9px; }
  .card-back .divider { width: 1px; height: 130px; background: var(--rule); margin: 0 20px; }
  .card-back .person-name { font-family: "Montserrat", Arial, sans-serif; font-weight: 700; font-size: 13px; }
  .card-back .person-title { font-size: 9.5px; color: var(--accent); margin-bottom: 10px; }
  .card-back ul { list-style: none; font-size: 9px; line-height: 1.75; color: var(--ink-soft); }
  .card-back li::before {
    content: ""; display: inline-block; width: 5px; height: 5px;
    background: var(--accent); margin-right: 6px; vertical-align: middle;
  }
  .card-back .card-bands { position: absolute; right: 0; bottom: 0; display: flex; width: 200px; height: 6px; }
  .card-back .card-bands .band-dark { flex: 1; background: var(--ink); }
  .card-back .card-bands .band-accent { width: 70px; background: var(--accent); }

  /* Standalone brand mark */
  .brand-panel {
    position: absolute; left: 80px; top: 680px;
    width: 400px; height: 110px;
    display: flex; align-items: center; justify-content: center;
  }
  .brand-panel .brand { font-size: 24px; gap: 12px; }
  .brand-panel .brand-square { width: 18px; height: 18px; }
</style>
</head>
<body>

  <section class="card card-front" aria-label="Business card front">
    <span class="brand"><span class="brand-square"></span>Grey Heron Realty</span>
    <span class="card-web">www.greyheronrealty.com</span>
  </section>

  <section class="card card-back" aria-label="Business card back">
    <span class="brand"><span class="brand-square"></span>Grey Heron Realty</span>
    <span class="divider"></span>
    <div class="card-details">
      <div class="person-name">Marcus Elden</div>
      <div class="person-title">President</div>
      <ul>
        <li>+1 555 014 2290</li>
        <li>+1 555 014 2291</li>
        <li>marcus@greyheronrealty.com</li>
        <li>www.greyheronrealty.com</li>
        <li>ABN 98 765 432 100</li>
      </ul>
    </div>
    <div class="card-bands"><span class="band-dark"></span><span class="band-accent"></span></div>
  </section>

  <section class="brand-panel" aria-label="Brand name">
    <span class="brand"><span class="brand-square"></span>Grey Heron Realty</span>
  </section>

  <section class="letterhead" aria-label="Letterhead">
    <div class="brand-row">
      <span class="brand"><span class="brand-square"></span>Grey Heron Realty</span>
    </div>
    <div class="letter-body">
      <p class="salutation">Dear Sir/Madam,</p>
      <p>Thank you for considering our team for your next property move. We look forward to helping you find a home that suits your plans and budget.</p>
      <p>Our agents know the local market well and work closely with every client, from first viewing through to final settlement, so each step stays clear and simple.</p>
      <p>We provide honest appraisals, careful marketing and regular updates. Whether you are buying, selling or leasing, our staff will guide you with patience and care at every stage.</p>
      <p>Please contact our office at any time to arrange a meeting or a free appraisal.</p>
    </div>
    <div class="sign-off">
      <div>Best Regards</div>
      <div class="signature">Marcus Elden</div>
      <div>President</div>
    </div>
    <footer class="letter-footer">
      <div class="company-line">Grey Heron Realty</div>
      <div class="footer-rule"></div>
      <div class="contact-row">
        <span><b>M:</b> +1 555 014 2290</span>
        <span><b>F:</b> +1 555 014 2291</span>
        <span><b>E:</b> marcus@greyheronrealty.com</span>
        <span><b>W:</b> www.greyheronrealty.com</span>
      </div>
      <div class="edge-bands"><span class="band-dark"></span><span class="band-accent"></span></div>
    </footer>
  </section>

</body>
</html>
```